Australian Wine export company Need a Wine label design

We need a wine label design for a new branded Australian wine based in South Australia called " KESTRELMOOR " .
We will use this brand name ' KESTRELMOOR' to marketing Australian Red wine and White wine into Chinese Market.
We would like to see the label designs that look classic and make consumers feel this is a superior quality Australian wine.
This label is to promote AUSTRALIAN WINE, need wine related and country related theme, need to give the consumer first impression that this wine is from AUSTRALIA.

Thanks

The following information are required to be presented on the wine label:

1) Brand Name: Kestrelmoor
2) Logo
3) Year of Vintage
4) Varietal
5) Place of production: South Australia
6) Fine Wine of Australia

Thanks.

Target Market(s)

Chinese market

Industry/Entity Type

Marketing

Requirements
Must have
• Need label design and renderings on the bottles.
Nice to have
• Label make consumers feel this is a superior quality Australian Wine.

```html
<!DOCTYPE html>
<html lang="en">
<head>
<meta charset="utf-8">
<title>Kestrelmoor – Australian Red Wine label options</title>
<link rel="stylesheet" href="https://fonts.googleapis.com/css2?family=Questrial&family=Marcellus&family=Marcellus+SC&family=IM+Fell+English&family=Cormorant+Garamond:wght@600&family=Federo&family=Lora:wght@700&display=swap">
<style>
  :root {
    --page-bg: #ffffff;
    --heading-ink: #000000;
    --label-edge: #1a0b0b;
    --label-mid: #8e1518;
    --label-core: #ed1c24;
    --label-ink: #ffffff;
    --laurel-tone: #c9b9b9;
  }
  * { margin: 0; padding: 0; box-sizing: border-box; }
  html, body {
    width: 1200px; height: 1000px; overflow: hidden;
    background: var(--page-bg);
  }
  .sheet {
    position: relative; width: 1200px; height: 1000px;
    font-family: "Questrial", sans-serif; color: var(--heading-ink);
  }
  .sheet-title {
    position: absolute; top: 18px; left: 0; width: 100%;
    text-align: center; font-size: 36px; font-weight: 400; letter-spacing: -0.5px;
  }
  .option {
    position: absolute; width: 292px;
  }
  .option-name {
    text-align: center; font-size: 48px; font-weight: 400; letter-spacing: -1px;
    line-height: 1; height: 64px;
  }
  .label {
    position: relative; width: 292px; height: 360px; margin-top: 8px;
    background: linear-gradient(90deg, var(--label-edge) 0%, var(--label-mid) 14%, var(--label-core) 30%, var(--label-core) 70%, var(--label-mid) 86%, var(--label-edge) 100%);
    color: var(--label-ink); text-align: center;
    font-family: "Questrial", sans-serif;
  }
  .varietal { position: absolute; top: 16px; width: 100%; font-size: 15.5px; }
  .vintage { position: absolute; top: 36px; width: 100%; font-size: 11px; }
  .laurel {
    position: absolute; top: 48px; left: 78px; width: 136px; height: 18px;
    background: linear-gradient(90deg, transparent, var(--laurel-tone) 20%, var(--laurel-tone) 80%, transparent);
    opacity: 0.55; border-radius: 9px;
  }
  .brand {
    position: absolute; top: 166px; left: 0; width: 100%;
    font-size: 44px; line-height: 1; color: var(--label-ink);
  }
  .brand--marcellus { font-family: "Marcellus", serif; }
  .brand--fell { font-family: "IM Fell English", serif; font-size: 46px; }
  .brand--lora { font-family: "Lora", serif; font-weight: 700; font-size: 41px; }
  .brand--federo { font-family: "Federo", sans-serif; font-size: 46px; }
  .brand--garamond { font-family: "Cormorant Garamond", serif; font-weight: 600; font-size: 48px; }
  .brand--caps { font-family: "Marcellus SC", serif; font-size: 36px; top: 172px; }
  .volume { position: absolute; top: 322px; width: 100%; font-size: 11.5px; }
  .strength { position: absolute; top: 339px; width: 100%; font-size: 11.5px; }
</style>
</head>
<body>
<main class="sheet">
  <h1 class="sheet-title">Boomerang at 65% of original</h1>

  <section class="option" style="left:49px; top:70px;">
    <h2 class="option-name">Original</h2>
    <div class="label">
      <p class="varietal">Australian Red Wine</p>
      <p class="vintage">2013</p>
      <div class="laurel" role="img" aria-label="Silver laurel branch ornament"></div>
      <p class="brand brand--marcellus">Kestrelmoor</p>
      <p class="volume">750 mL</p>
      <p class="strength">14% ALC/VOL</p>
    </div>
  </section>

  <section class="option" style="left:454px; top:70px;">
    <h2 class="option-name">Option 1</h2>
    <div class="label">
      <p class="varietal">Australian Red Wine</p>
      <p class="vintage">2013</p>
      <div class="laurel" role="img" aria-label="Silver laurel branch ornament"></div>
      <p class="brand brand--fell">Kestrelmoor</p>
      <p class="volume">750 mL</p>
      <p class="strength">14% ALC/VOL</p>
    </div>
  </section>

  <section class="option" style="left:858px; top:69px;">
    <h2 class="option-name">Option 2</h2>
    <div class="label">
      <p class="varietal">Australian Red Wine</p>
      <p class="vintage">2013</p>
      <div class="laurel" role="img" aria-label="Silver laurel branch ornament"></div>
      <p class="brand brand--lora">Kestrelmoor</p>
      <p class="volume">750 mL</p>
      <p class="strength">14% ALC/VOL</p>
    </div>
  </section>

  <section class="option" style="left:49px; top:556px;">
    <h2 class="option-name">Option 3</h2>
    <div class="label">
      <p class="varietal">Australian Red Wine</p>
      <p class="vintage">2013</p>
      <div class="laurel" role="img" aria-label="Silver laurel branch ornament"></div>
      <p class="brand brand--federo">Kestrelmoor</p>
      <p class="volume">750 mL</p>
      <p class="strength">14% ALC/VOL</p>
    </div>
  </section>

  <section class="option" style="left:454px; top:556px;">
    <h2 class="option-name">Option 4</h2>
    <div class="label">
      <p class="varietal">Australian Red Wine</p>
      <p class="vintage">2013</p>
      <div class="laurel" role="img" aria-label="Silver laurel branch ornament"></div>
      <p class="brand brand--garamond">Kestrelmoor</p>
      <p class="volume">750 mL</p>
      <p class="strength">14% ALC/VOL</p>
    </div>
  </section>

  <section class="option" style="left:857px; top:555px;">
    <h2 class="option-name">Option 5</h2>
    <div class="label">
      <p class="varietal">Australian Red Wine</p>
      <p class="vintage">2013</p>
      <div class="laurel" role="img" aria-label="Silver laurel branch ornament"></div>
      <p class="brand brand--caps">KESTRELMOOR</p>
      <p class="volume">750 mL</p>
      <p class="strength">14% ALC/VOL</p>
    </div>
  </section>
</main>
</body>
</html>
```